Letterhead for Dorian Welk

I need a letterhead based on the business card design

Industry/Entity Type

Business

Requirements
Must have
• Footer: Dorian Welk Naturopath
Shop 4123c, 46 Carrow Lane, Sydney 2000

```html
<!DOCTYPE html>
<html lang="en">
<head>
<meta charset="utf-8">
<title>Dorian Welk Naturopath – Letterhead</title>
<link href="https://fonts.googleapis.com/css2?family=Exo+2:wght@400;500&family=Allura&display=swap" rel="stylesheet">
<style>
  :root {
    --canvas: #f2f2f2;
    --paper: #fafafa;
    --brand-orange: #f0902c;
    --leaf-tint: #f6d3b1;
    --leaf-tint-soft: #f9e2cc;
    --ink: #3a3a3a;
    --ink-soft: #555555;
    --rule: #444444;
  }
  * { box-sizing: border-box; margin: 0; padding: 0; }
  html, body {
    width: 1200px; height: 1000px; overflow: hidden;
    background: var(--canvas);
  }
  .canvas { position: relative; width: 1200px; height: 1000px; }

  .sheet {
    position: absolute; top: 193px;
    width: 439px; height: 613px;
    background: var(--paper);
    overflow: hidden;
    font-family: "Exo 2", sans-serif;
    color: var(--ink);
  }
  .sheet--plain { left: 133px; }
  .sheet--leaf  { left: 614px; width: 434px; }

  .leaf-backdrop {
    position: absolute; left: -40px; top: 50px;
    width: 230px; height: 505px;
    border-radius: 10% 90% 60% 40% / 8% 60% 40% 92%;
    background: linear-gradient(160deg, var(--leaf-tint-soft) 0%, var(--leaf-tint) 55%, var(--leaf-tint-soft) 100%);
    opacity: 0.85;
  }

  .brand {
    position: absolute; left: 0; right: 0; top: 48px;
    text-align: center; color: var(--brand-orange);
    font-weight: 500;
  }
  .brand__name { font-size: 26px; letter-spacing: 0.5px; line-height: 28px; text-transform: uppercase; }
  .brand__field { font-size: 14px; letter-spacing: 2.5px; line-height: 18px; margin-top: 42px; text-transform: uppercase; }

  .letter {
    position: absolute; left: 71px; width: 295px;
    font-size: 6.6px; line-height: 10.7px;
    color: var(--ink-soft);
  }
  .letter p { text-align: justify; position: absolute; left: 0; width: 295px; }
  .letter .salutation { top: 0; }
  .letter .para-1 { top: 23px; }
  .letter .para-2 { top: 133px; }
  .letter .para-3 { top: 223px; }
  .letter .closing { top: 278px; }

  .signature {
    position: absolute; left: 288px; top: 472px;
    font-family: "Allura", cursive; font-size: 24px; color: #222;
  }

  .footer {
    position: absolute; left: 71px; width: 295px; top: 579px;
    border-top: 1px solid var(--rule);
    text-align: center;
  }
  .footer__name { color: var(--brand-orange); font-size: 8.5px; margin-top: 3px; line-height: 11px; }
  .footer__contact { font-size: 5.4px; color: var(--ink); line-height: 9px; display: flex; justify-content: center; gap: 2px; align-items: center; }
  .footer__contact span { display: inline-flex; align-items: center; gap: 1px; }
  .footer__contact svg { width: 5px; height: 5px; fill: var(--brand-orange); }
</style>
</head>
<body>
<div class="canvas">

  <section class="sheet sheet--plain">
    <div class="brand" aria-label="Dorian Welk Naturopathy">
      <div class="brand__name">Dorian Welk</div>
      <div class="brand__field">Naturopathy</div>
    </div>
    <div class="letter" style="top:174px">
      <p class="salutation">Dear Client,</p>
      <p class="para-1">Lorem ipsum dolor sit amet, consectetur adipiscing elit. Nulla sodales nisi vitae Lorem ipsum dolor sit amet, consectetur adipiscing elit. Suspendisse feugiat eros nisl, a facilisis risus eleifend sed. Aliquam mauris enim, fermentum eu lacinia sit amet, laoreet eu leo. Nullam eleifend nulla in libero tristique, ac vulputate odio tincidunt. Etiam non condimentum tortor. Integer suscipit neque nec odio porttitor cursus. Phasellus a sapien blandit, suscipit justo id, condimentum ante. Morbi tristique justo risus, id mattis dui molestie ut. Nullam volutpat ut quam commodo faucibus. Pellentesque urna est, interdum in elit quis, pharetra elementum orci. Nam pharetra velit molestie justo placerat sceleris-que.</p>
      <p class="para-2">Nulla tincidunt molestie libero vel pretium. Donec condimentum nulla sit amet risus semper imperdi-et. Duis congue eros nec diam blandit, et pellentesque sapien auctor. Curabitur iaculis enim lectus, in imperdiet mauris mattis eget. Etiam ac ornare metus. Mauris risus leo, egestas at dolor a, ultrices adipiscing est. Nunc faucibus scelerisque mollis. Pellentesque aliquet mauris tellus, id dignissim risus viverra et. Mauris venenatis lobortis eros. Nam id diam in ligula malesuada feugiat. Cras turpis felis, aliquet id mauris elementum, feugiat ultricies nisl.</p>
      <p class="para-3">Nullam auctor venenatis metus, eu pulvinar sapien dapibus non. Cum sociis natoque penatibus et magnis dis parturient montes, nascetur ridiculus mus. Praesent sed lorem eget tortor volutpat dictum vel vel ipsum. Morbi ac mauris sed elit dictum volutpat. Morbi pulvinar non nisi in ultrices. Pellentesque quis mi in risus eleifend adipiscing.</p>
      <p class="closing">Best regards,</p>
    </div>
    <div class="signature">Dorian Welk</div>
    <footer class="footer">
      <div class="footer__name">Dorian Welk Naturopath</div>
      <div class="footer__contact">
        <span><svg viewBox="0 0 10 10"><path d="M5 0a3.6 3.6 0 0 0-3.6 3.6C1.4 6.3 5 10 5 10s3.6-3.7 3.6-6.4A3.6 3.6 0 0 0 5 0zm0 5a1.4 1.4 0 1 1 0-2.8A1.4 1.4 0 0 1 5 5z"/></svg>Shop 4123c, 46 Carrow Lane, Sydney 2000</span>
        <span><svg viewBox="0 0 10 10"><circle cx="5" cy="5" r="5"/></svg>dorianwelk.com.au</span>
        <span><svg viewBox="0 0 10 10"><circle cx="5" cy="5" r="5"/></svg>verdantdrops</span>
      </div>
    </footer>
  </section>

  <section class="sheet sheet--leaf">
    <div class="leaf-backdrop" role="img" aria-label="Large faint peach leaf decoration along the left edge"></div>
    <div class="brand" aria-label="Dorian Welk Naturopathy">
      <div class="brand__name">Dorian Welk</div>
      <div class="brand__field">Naturopathy</div>
    </div>
    <div class="letter" style="top:174px">
      <p class="salutation">Dear Client,</p>
      <p class="para-1">Lorem ipsum dolor sit amet, consectetur adipiscing elit. Nulla sodales nisi vitae Lorem ipsum dolor sit amet, consectetur adipiscing elit. Suspendisse feugiat eros nisl, a facilisis risus eleifend sed. Aliquam mauris enim, fermentum eu lacinia sit amet, laoreet eu leo. Nullam eleifend nulla in libero tristique, ac vulputate odio tincidunt. Etiam non condimentum tortor. Integer suscipit neque nec odio porttitor cursus. Phasellus a sapien blandit, suscipit justo id, condimentum ante. Morbi tristique justo risus, id mattis dui molestie ut. Nullam volutpat ut quam commodo faucibus. Pellentesque urna est, interdum in elit quis, pharetra elementum orci. Nam pharetra velit molestie justo placerat sceleris-que.</p>
      <p class="para-2">Nulla tincidunt molestie libero vel pretium. Donec condimentum nulla sit amet risus semper imperdi-et. Duis congue eros nec diam blandit, et pellentesque sapien auctor. Curabitur iaculis enim lectus, in imperdiet mauris mattis eget. Etiam ac ornare metus. Mauris risus leo, egestas at dolor a, ultrices adipiscing est. Nunc faucibus scelerisque mollis. Pellentesque aliquet mauris tellus, id dignissim risus viverra et. Mauris venenatis lobortis eros. Nam id diam in ligula malesuada feugiat. Cras turpis felis, aliquet id mauris elementum, feugiat ultricies nisl.</p>
      <p class="para-3">Nullam auctor venenatis metus, eu pulvinar sapien dapibus non. Cum sociis natoque penatibus et magnis dis parturient montes, nascetur ridiculus mus. Praesent sed lorem eget tortor volutpat dictum vel vel ipsum. Morbi ac mauris sed elit dictum volutpat. Morbi pulvinar non nisi in ultrices. Pellentesque quis mi in risus eleifend adipiscing.</p>
      <p class="closing">Best regards,</p>
    </div>
    <div class="signature">Dorian Welk</div>
    <footer class="footer">
      <div class="footer__name">Dorian Welk Naturopath</div>
      <div class="footer__contact">
        <span><svg viewBox="0 0 10 10"><path d="M5 0a3.6 3.6 0 0 0-3.6 3.6C1.4 6.3 5 10 5 10s3.6-3.7 3.6-6.4A3.6 3.6 0 0 0 5 0zm0 5a1.4 1.4 0 1 1 0-2.8A1.4 1.4 0 0 1 5 5z"/></svg>Shop 4123c, 46 Carrow Lane, Sydney 2000</span>
        <span><svg viewBox="0 0 10 10"><circle cx="5" cy="5" r="5"/></svg>dorianwelk.com.au</span>
        <span><svg viewBox="0 0 10 10"><circle cx="5" cy="5" r="5"/></svg>verdantdrops</span>
      </div>
    </footer>
  </section>

</div>
</body>
</html>
```